Need Business Card Design, Letterhead and a Basic Form layout based on Existing Logo

We need (1) a business card design, (2) a letterhead design and (3) a basic form layout for an international holding company. This holding company has just formed two (2) sub-companies. The logo is the same for each company with only a simple word change for each company. The business card, letterhead and form design will be essentially the same for each company... with only the one word change being different.
The names of the companies are as follows:
1. Kestrel Trust Services
2. Kestrel Immigration Services
The design for the business card, letterhead and Form must be strong, clean and classy.
Our clients will be older, wealthy and mostly Asian. The design must project strength, stability and confidence.
The card may contain the following data:
1. The Logo
2. The name of the person
3. The title of the person
4. The address of the company
5. The Company Phone number
6. The personal mobile number
7. The Skype number (VOIP)
8. The WICKR number (IM)
9. The email
10. The website
We will attach AI files of our logo for the "Kestrel Trust Services" company in the colors Black/White and Blue in both Horizontal and Vertical format... We have also included separate files of the logo icon.
We uploaded the AI files to give the designer the maximum options regarding color and effects. We included the separate files for the icon because we would like to give the designer the option of a watermark. Also, we think it might be nice to highlight the icon on the back of the card perhaps with the website address.
We are not sure which colors or color combinations would be best for these two companies. We know the colors must again project strength, stability and confidence. Perhaps, a combination that might include Tan, Black and White... not sure... need design help... remember this has to have the presence of a bank-like institution... no cartoonish designs or flashy color combinations... please.
The basic form layout will be used for various questionaires, input sheets and instructions.... etc.
NOTE: The fonts used in the logo are Trajan Pro Bold for word "KESTREL" and Trajan Pro Regular for "XXXXXXXXX SERVICES".

```html
<!DOCTYPE html>
<html lang="en">
<head>
<meta charset="utf-8">
<title>Kestrel Trust Services — Stationery</title>
<link href="https://fonts.googleapis.com/css2?family=PT+Sans:wght@400;700&family=Arimo:wght@400;700&display=swap" rel="stylesheet">
<style>
  :root {
    --ink: #111111;
    --black: #050505;
    --band-hi: #2a2a2a;
    --paper: #fbfbfb;
    --stage: #dcdcdc;
    --grey-strip: #6b6b6b;
    --text: #3a3a3a;
    --muted: #5a5a5a;
  }
  * { box-sizing: border-box; margin: 0; padding: 0; }
  html, body { width: 1200px; height: 1050px; overflow: hidden; }
  body { background: var(--stage); font-family: "PT Sans", sans-serif; color: var(--text); position: relative; }

  .sheet { position: absolute; background: var(--paper); overflow: hidden; }
  .band { position: absolute; top: 0; bottom: 0; left: 0;
    background: linear-gradient(160deg, var(--band-hi) 0%, var(--black) 28%, var(--black) 100%); }

  .brand { position: absolute; display: flex; align-items: center; gap: 12px; }
  .brand-mark { border: 3px solid currentColor; flex: none; }
  .brand-name { font-family: "PT Sans", sans-serif; font-weight: 400; line-height: 1; color: inherit; white-space: nowrap; }

  /* Letterhead */
  .letterhead { left: 475px; top: 78px; width: 695px; height: 892px; }
  .letterhead .band { width: 109px; }
  .letterhead .brand { left: 62px; top: 50px; color: var(--ink); }
  .letterhead .brand-mark { width: 52px; height: 52px; background: var(--paper); }
  .letterhead .brand-name { font-size: 22px; }
  .letter-body { position: absolute; left: 134px; top: 150px; width: 516px; font-size: 11.6px; line-height: 16.2px; color: var(--text); }
  .letter-body p { margin-bottom: 16px; }
  .letter-body p.gap { margin-top: 16px; }
  .letter-body .closing { margin-top: 42px; }
  .band-contacts { position: absolute; left: 0; width: 102px; top: 780px; text-align: right; color: #e8e8e8; font-family: "Arimo", sans-serif; font-size: 8.6px; line-height: 12.2px; }
  .band-contacts i { display: inline-block; width: 5px; height: 5px; border: 1px solid #bbb; margin-left: 4px; vertical-align: middle; }
  .letter-address { position: absolute; left: 109px; right: 0; top: 848px; text-align: center; font-family: "Arimo", sans-serif; font-size: 8.8px; line-height: 11px; color: var(--muted); }

  /* Envelope back */
  .envelope-back { left: 30px; top: 290px; width: 445px; height: 318px; background: #f2f2f2; }
  .envelope-back .flap-band { position: absolute; left: 0; right: 0; top: 2px; height: 86px; background: linear-gradient(90deg, #111 0%, #222 50%, #111 100%); }
  .envelope-back .flap-band .brand { left: 348px; top: 26px; color: #fff; }
  .envelope-back .flap-band .brand-mark { width: 28px; height: 28px; border-width: 2px; }
  .envelope-back .web { position: absolute; left: 325px; top: 66px; font-family: "Arimo", sans-serif; font-size: 9px; color: #ddd; }

  /* Envelope front */
  .envelope { left: 30px; top: 640px; width: 445px; height: 310px; }
  .envelope .band { width: 54px; bottom: 6px; }
  .envelope .strip { position: absolute; left: 0; right: 0; bottom: 0; height: 6px; background: var(--grey-strip); }
  .envelope .brand { left: 30px; top: 24px; color: var(--ink); }
  .envelope .brand-mark { width: 50px; height: 50px; background: var(--paper); }
  .envelope .brand-name { font-size: 18px; }
  .envelope-address { position: absolute; left: 77px; top: 271px; font-family: "Arimo", sans-serif; font-size: 8.6px; line-height: 11px; color: var(--muted); }

  /* Card back */
  .card-back { left: 75px; top: 247px; width: 288px; height: 157px; background: linear-gradient(200deg, #2b2b2b 0%, #0a0a0a 40%, #050505 100%); }
  .card-back .brand { left: 50px; top: 60px; color: #fff; gap: 10px; }
  .card-back .brand-mark { width: 34px; height: 34px; border-width: 2px; }
  .card-back .brand-name { font-size: 14px; }
  .card-back .web { position: absolute; left: 105px; top: 128px; font-family: "Arimo", sans-serif; font-size: 6.5px; color: #ddd; }

  /* Card front */
  .card-front { left: 75px; top: 427px; width: 285px; height: 158px; }
  .card-front .band { width: 35px; bottom: 20px; }
  .card-front .footer { position: absolute; left: 0; right: 0; bottom: 0; height: 20px; background: var(--grey-strip); color: #fff; font-family: "Arimo", sans-serif; font-size: 5.6px; line-height: 7px; text-align: right; padding: 3px 22px 0 0; }
  .card-front .brand { left: 20px; top: 25px; color: var(--ink); gap: 8px; }
  .card-front .brand-mark { width: 28px; height: 28px; border-width: 2px; background: var(--paper); }
  .card-front .brand-name { font-size: 11px; }
  .person { position: absolute; left: 63px; top: 76px; font-family: "Arimo", sans-serif; }
  .person .name { font-size: 7.6px; font-weight: 700; color: var(--ink); }
  .person .title { font-size: 6.4px; color: var(--muted); margin-top: 1px; }
  .card-contacts { position: absolute; right: 18px; top: 76px; text-align: right; font-family: "Arimo", sans-serif; font-size: 6.4px; line-height: 8.3px; color: var(--text); }
  .card-contacts i { display: inline-block; width: 4px; height: 4px; border: 1px solid #888; margin-left: 4px; vertical-align: middle; }
</style>
</head>
<body>

  <section class="sheet envelope-back" aria-label="Envelope back">
    <div class="flap-band">
      <div class="brand"><span class="brand-mark"></span></div>
      <div class="web">www.kestreltrust.com</div>
    </div>
  </section>

  <section class="sheet card-back" aria-label="Business card back">
    <div class="brand">
      <span class="brand-mark"></span>
      <div class="brand-name">Kestrel Trust Services</div>
    </div>
    <div class="web">www.kestreltrust.com</div>
  </section>

  <section class="sheet card-front" aria-label="Business card front">
    <div class="band" role="img" aria-label="Dark side band with faint angled pattern"></div>
    <div class="brand">
      <span class="brand-mark"></span>
      <div class="brand-name">Kestrel Trust Services</div>
    </div>
    <div class="person">
      <div class="name">MARTIN OLSEN</div>
      <div class="title">Managing Director</div>
    </div>
    <div class="card-contacts">
      502-3170-4482<i></i><br>
      502-3170-4482 (Local)<i></i><br>
      502-3170-4482 (Int'l)<i></i><br>
      kestreldirect<i></i><br>
      martin@kestreltrust.com<i></i><br>
      www.kestreltrust.com<i></i>
    </div>
    <div class="footer">
      Centro Empresarial Las Brisas, Office #10<br>
      Esquina Calle del Arco y Callejón San Jerónimo | Antigua, Guatemala
    </div>
  </section>

  <section class="sheet envelope" aria-label="Envelope front">
    <div class="band" role="img" aria-label="Dark side band with faint angled pattern"></div>
    <div class="strip"></div>
    <div class="brand">
      <span class="brand-mark"></span>
      <div class="brand-name">Kestrel Trust Services</div>
    </div>
    <div class="envelope-address">
      Centro Empresarial Las Brisas, Office #10<br>
      Esquina Calle del Arco y Callejón San Jerónimo | Antigua, Guatemala
    </div>
  </section>

  <section class="sheet letterhead" aria-label="Letterhead">
    <div class="band" role="img" aria-label="Dark side band with faint angled pattern"></div>
    <div class="brand">
      <span class="brand-mark"></span>
      <div class="brand-name">Kestrel Trust Services</div>
    </div>
    <div class="letter-body">
      <p>Lorem ipsum dolor sit amet, consectetur adipiscing elit. Duis sed aliquet neque. Fusce mollis placerat leo eu faucibus. Suspendisse suscipit egestas nunc, consequat euismod quam elementum venenatis. Nulla vitae nulla id mauris dictum imperdiet in vitae augue. Suspendisse fringilla bibendum ultrices.</p>
      <p>Sed rhoncus, nisi nec egestas tempus, orci velit ullamcorper dolor, malesuada molestie libero tellus in justo. Duis pharetra, turpis vel ultrices consequat, est ante laoreet nisi, et imperdiet ligula ipsum non quam. In tristique consequat diam, sed semper dolor aliquet et. Cum sociis natoque penatibus et magnis dis parturient montes, nascetur ridiculus mus. Duis sit amet ante mauris, a sodales tellus. Phasellus ante eros, lacinia at eleifend eu, laoreet sed nibh. Nulla rhoncus erat vitae dolor aliquam varius pretium lectus accumsan.</p>
      <p class="gap">Aliquam quis lorem eget nibh dignissim accumsan. Proin vitae lectus pretium justo molestie pellentesque. Fusce ultrices risus vitae justo adipiscing id consectetur elit sagittis. Integer nec dapibus tellus. Donec ultricies massa a dolor eleifend ut adipiscing felis feugiat. Praesent fermentum sem felis, vitae vulputate odio.</p>
      <p>Curabitur faucibus leo quis velit molestie in fringilla ligula mollis. Pellentesque aliquet dolor ut nibh tempor sed vehicula arcu malesuada. Maecenas eget justo at augue molestie ullamcorper non eu est. Cras varius ullamcorper malesuada. Proin ut enim imperdiet augue pulvinar iaculis eget nec ipsum. Fusce sed orci mi. Etiam tristique suscipit ligula non volutpat. Nullam lobortis, enim sed faucibus faucibus, lacus risus euismod ligula, at interdum justo libero a elit. Pellentesque sem ligula, tempor a faucibus auctor, gravida et ante. Donec tristique imperdiet eros et vulputate. Cras id purus id mi volutpat egestas. Cras tellus velit, tristique at dignissim et, tincidunt at felis. Maecenas vestibulum felis eget mauris pellentesque gravida. Nunc commodo tincidunt ornare. Suspendisse quis volutpat lectus. Nunc sed dui sit amet nulla vulputate congue et imperdiet mi.</p>
      <p class="closing">Sincerely</p>
    </div>
    <div class="band-contacts">
      502-3170-4482 (Local)<i></i><br>
      502-3170-4482 (Int'l)<i></i><br>
      kestreldirect<i></i><br>
      info@kestreltrust.com<i></i><br>
      www.kestreltrust.com<i></i>
    </div>
    <div class="letter-address">
      Centro Empresarial Las Brisas, Office #10<br>
      Esquina Calle del Arco y Callejón San Jerónimo | Antigua, Guatemala
    </div>
  </section>

</body>
</html>
```